Immobilienfirma sucht Flyerdesign
Zielgruppe
Wir sind ein Immobilienmaklerbüro spezialisiert auf den Verkauf von Einfamilienhäusern und Baugrundstücken im Umland von Berlin (Havelland & Oberhavel).
Zielgruppe des Flyers sind ausschließlich Eigentümer von Immobilien die verkaufen möchten.
Wir benötigen 6 - 8 Mal pro Jahre neue Flyer. Wir haben daher Interesse an einer regelmäßigen Zusammenarbeit.
Aufgabenstellung
Der Flyer soll im Format A 4 sein (hochkant).
Es soll eher Text sprechen, da wir möglichst viel Informationen transportieren möchten.
Wir richten uns ausschließlich an die Eigentümer (Verkäufer) von Immobilie die wir begeistern möchten gerade über uns zu verkaufen.
Unser Alleinstellungsmerkmal ist als "Makler OHNE Schilder" zu arbeiten, im Gegensatz zu unseren Mitbewerbern die die ganze Stadt zuplakatieren mit Werbebannern an Gartenzäunen und Straßenecken, Maklerschildern und Maklergalgen vor den zum Verkauf stehen Häusern etc.
Wir verkaufen diskret und bieten Verkäufern ein Komplettpaket von der unverbindlichen Erstberatung, über die kostenlose Wertermittlung, den kostenlosen Energieausweis, den kompletten Verkauf (natürlich ohne Schilder) bis zum Notartermin. Auch danach sind wir für den Verkäufer da und suchen ihm eine neue Bleibe und helfen auch mit Umzugsfirmen etc.
Komplettprogramm für Verkäufer - und selbstverständlich für Verkäufer komplett KOSTENLOS !
Als Bilder dachten wir an ein Portraitfoto von mir das mit Angebot ein Gesicht bekommt und der Kunde weiß wer ihm gegenüber sitzt, sowie ein eycatcher Bild.
Wir bieten unseren Kunden einen diskreten und schnellen Verkauf. Komplettservice : Kostenlose Wertermittlung, kostenloser Energieausweis, Übernahme des kompletten Verkaufs bis zum Notartermin, Hilfe bei der Suche nach neuer Immobilie, Hilfe beim Umzug.

```html
<!DOCTYPE html>
<html lang="de">
<head>
<meta charset="utf-8">
<title>Unser Service – Immobilienmanagement Kestermann</title>
<link href="https://fonts.googleapis.com/css2?family=Open+Sans:ital,wght@0,300;0,400;0,700;1,400&family=Arimo:ital@1&display=swap" rel="stylesheet">
<style>
  :root {
    --ink: #3f3f3f;
    --ink-soft: #4a4a4a;
    --rule: #8a8a8a;
    --accent: #8b1010;
    --paper: #ffffff;
    --photo-dark: #3c3f3b;
    --photo-mid: #7d837c;
    --photo-light: #b4b9b2;
    --overlay-text: #ffffff;
  }
  * { margin: 0; padding: 0; box-sizing: border-box; }
  html, body { width: 1200px; height: 849px; overflow: hidden; background: var(--paper); }
  .spread { position: relative; width: 1200px; height: 849px; background: var(--paper); font-family: "Open Sans", sans-serif; color: var(--ink); }

  .brand-dot { position: absolute; left: 36px; top: 21px; width: 77px; height: 77px; border-radius: 50%; background: var(--ink); }
  .header-rule { position: absolute; left: 115px; top: 56px; width: 269px; height: 1px; background: var(--rule); }
  .brand-name { position: absolute; left: 398px; top: 38px; font-size: 10.5px; line-height: 14px; color: var(--ink); font-weight: 400; }

  .page-title { position: absolute; left: 101px; top: 255px; font-size: 50px; font-weight: 700; letter-spacing: 0.5px; color: var(--ink); line-height: 1; }

  .lead { position: absolute; left: 100px; top: 315px; width: 122px; text-align: right; font-family: "Arimo", sans-serif; font-style: italic; font-size: 9.4px; line-height: 12.1px; color: var(--accent); }
  .column-rule { position: absolute; left: 230px; top: 317px; width: 1px; height: 456px; background: var(--ink-soft); }
  .body-copy { position: absolute; left: 240px; top: 315px; width: 262px; font-size: 10.1px; line-height: 12.1px; color: var(--ink-soft); hyphens: auto; }
  .body-copy p + p { margin-top: 12.1px; }

  .footer { position: absolute; left: 36px; top: 807px; font-size: 10.5px; color: var(--ink); }
  .footer-rule { position: absolute; left: 84px; top: 815px; width: 481px; height: 1px; background: var(--rule); }

  .hero { position: absolute; left: 638px; top: 37px; width: 529px; height: 777px; overflow: hidden;
    background: radial-gradient(ellipse at 60% 55%, var(--photo-mid) 0%, var(--photo-dark) 60%),
                linear-gradient(160deg, var(--photo-light) 0%, var(--photo-mid) 35%, var(--photo-dark) 100%); }
  .hero-claim { position: absolute; color: var(--overlay-text); font-weight: 300; line-height: 1; white-space: nowrap; }
  .claim-small { font-size: 20px; }
  .claim-big { font-size: 50px; letter-spacing: 0.5px; }
  .claim-line-1 { left: 10px; top: 682px; }
  .claim-line-2 { left: 84px; top: 722px; }
</style>
</head>
<body>
<div class="spread">
  <div class="brand-dot"></div>
  <div class="header-rule"></div>
  <div class="brand-name">Immobilienmanagement<br>Kestermann</div>

  <h1 class="page-title">UNSER SERVICE</h1>

  <p class="lead">Wir sind seit nunmehr 20 Jahren im Immobilienma&shy;nagement tätig. Wir haben zudem 6 Jahre Erfahrung im Immobilienvertrieb im Ausland gesammelt.</p>
  <div class="column-rule"></div>

  <div class="body-copy">
    <p>Wir bieten Ihnen einen umfassenden Komplettservice rund um Ihre Immobilie. Wir haben nunmehr 20 Jahre Erfahrung im Immobilienbereich. Wir begutachten kostenfrei und unverbindlich Ihre Immobilie. Auf Wunsch erhalten Sie gerne eine kostenfreie Marktwertanalyse.</p>
    <p>Wir bieten Ihnen einen sehr diskreten Verkauf, OHNE das Aufstellen von Verkaufsschildern / Werbeschildern, ohne Adressnennung etc.</p>
    <p>Wir erzielen für Ihre Immobilie den maximalen Verkaufspreis, da wir nicht dutzende Immobilien gleichzeitig verkaufen sondern uns mit vollem Zeiteinsatz speziell Ihrer Immobilie und deren Verkauf /Vermietung widmen.</p>
    <p>Klasse statt Masse - wir haben ganz bewußt nicht 100 Immobilien gleichzeitig im Bestand. Daher können wir Ihre Immobilie schnell und zum Höchstpreis verkaufen, da wir genug Zeit haben uns dem Objekt zu widmen.</p>
    <p>Wir bieten Ihnen weiterhin einen kostenfreien Energieausweis der für den Verkauf gesetzlich vorgeschrieben ist.</p>
    <p>Wir arbeiten sehr diskret - grundsätzlich OHNE Maklerschilder. Ihre Nachbarn werden daher nicht schon Wochen vor dem Verkauf informiert. Wir arbeiten sehr diskret und professionell.</p>
    <p>Wir erstellen zudem professionelle Fotos Ihrer Immobilie und auf Wunsch auch ein Präsentationsvideo.</p>
    <p>Bitte rufen Sie uns einfach unverbindlich für ein Erstgespräch an. Wir vermarkten Ihre Immobilie genau nach Ihren Wünschen - ganz individuell nach Ihren Vorgaben.</p>
  </div>

  <div class="footer">Seite 03</div>
  <div class="footer-rule"></div>

  <div class="hero" role="img" aria-label="Schwarzweißfoto: alte Buntbartschlüssel an einem Ring auf einem Holztisch">
    <div class="hero-claim claim-line-1"><span class="claim-small">Wir </span><span class="claim-big">ERZIELEN</span></div>
    <div class="hero-claim claim-line-2"><span class="claim-big">MAXIMALE </span><span class="claim-small">Preise!</span></div>
  </div>
</div>
</body>
</html>
```